Plakat-Design  für Laufverein
Plakat-Design für Laufverein
Zielgruppe
Wir sind ein Laufverein der dieses Jahr zum 7. Mal eine Laufveranstaltung organisiert.
Dieses Jahr möchten wir aber neue Wege gehen.
Der Name der gesamten Veranstaltung 'Sonnhang im Schwung'
Datum der Veranstaltung ist der 21.6.2020, Beginn Kinderläufe ab 9:30 Uhr, Beginn Hauptlauf und 'Quick 2 easy Dash' 10:30 Uhr)
Die Veranstaltung besteht
- aus einem 10 KM Hauptlauf inkl. Zeitnehmung (100,00 Tagessieg Prämie für 1. Dame und 1. Herr)
- einem 'Quick 2 Easy Dash' - 5km - OHNE Zeitnehmung. Unter allen Teilnehmern wird je 1 Paar Damen- und 1 Paar Herrenlaufschuhe verlost mit der Startnummer bei der Siegerehrung )
- Kinderläuf mit 600 m
- Schülerlauf mit 1050 m
Rahmenprogramm: grosse Tombola, Ort der Veranstaltung ist das 'talstation Kolbing', Parkplätze und Duschen gratis vorhanden.
Aufgabenstellung
Logoleiste für ca. 15 Sponsoren vorsehen.
Wichtig wäre sowohl die 'ambitionierten Läufer' für den 10 KM Lauf (Preisgeld für Tagessieg M / W) sowie die Läufer die gerne in der Masse untergehen für den 'Quick 2 Easy Dash' anzusprechen. Kinder nur als Zusatzangebot.
stockbilder wenn möglich von www.bilderhafenstock.de verwenden.

```html
<!DOCTYPE html>
<html lang="de">
<head>
<meta charset="utf-8">
<title>Sonnhang im Schwung 21.6.2020</title>
<link rel="stylesheet" href="https://fonts.googleapis.com/css2?family=Passion+One:wght@400;700&family=Nunito+Sans:wght@400;700;800&display=swap">
<style>
  :root {
    --sun: #ffd600;
    --sky: #00b4e6;
    --white: #ffffff;
    --grass-light: #b9d85a;
    --grass-dark: #4f8f1e;
    --ink: #333333;
  }
  * { box-sizing: border-box; margin: 0; padding: 0; }
  html, body { width: 849px; height: 1200px; overflow: hidden; background: var(--white); }
  .poster { position: relative; width: 849px; height: 1200px; overflow: hidden; font-family: "Nunito Sans", sans-serif; }
  .hero-photo {
    position: absolute; left: 0; top: 0; width: 849px; height: 1018px;
    background:
      radial-gradient(ellipse at 80% 20%, #f4efe6 0%, rgba(244,239,230,0) 45%),
      radial-gradient(ellipse at 85% 60%, #2e9fe0 0%, rgba(46,159,224,0) 30%),
      linear-gradient(180deg, #e8e2d6 0%, #c9c6a4 40%, var(--grass-light) 70%, var(--grass-dark) 100%);
  }
  .shapes { position: absolute; left: 0; top: 0; }
  .title {
    position: absolute; left: 54px; top: 60px;
    font-family: "Passion One", sans-serif; font-weight: 700;
    font-size: 72px; line-height: 1; color: var(--white);
    transform: rotate(-4deg); transform-origin: left bottom; white-space: nowrap;
  }
  .date {
    position: absolute; left: 322px; top: 136px;
    font-family: "Passion One", sans-serif; font-weight: 700;
    font-size: 126px; line-height: 1; color: var(--sky);
    transform: rotate(-3deg); letter-spacing: -2px; white-space: nowrap;
  }
  .venue {
    position: absolute; left: 592px; top: 278px;
    font-family: "Passion One", sans-serif; font-size: 26px;
    color: var(--sun); transform: rotate(-4deg); white-space: nowrap;
  }
  .races { position: absolute; left: 37px; top: 284px; color: var(--white); }
  .races-heading { font-family: "Passion One", sans-serif; font-weight: 700; font-size: 52px; line-height: 1; margin-bottom: 22px; }
  .race { margin-bottom: 26px; }
  .race-name { font-weight: 800; font-size: 31px; line-height: 1.2; white-space: nowrap; }
  .race-detail { font-size: 27px; line-height: 1.72; }
  .badge {
    position: absolute; border-radius: 50%; display: flex; flex-direction: column;
    align-items: center; justify-content: center; text-align: center;
  }
  .badge-prize { left: 505px; top: 437px; width: 184px; height: 184px; background: var(--sun); z-index: 3; }
  .badge-raffle { left: 450px; top: 572px; width: 204px; height: 204px; background: var(--white); z-index: 2; }
  .badge-service { left: 495px; top: 741px; width: 204px; height: 204px; background: var(--sky); z-index: 1; }
  .badge-title { font-family: "Passion One", sans-serif; font-weight: 700; line-height: 1; white-space: nowrap; }
  .badge-prize .badge-title { color: var(--white); font-size: 38px; }
  .badge-prize .badge-text { color: var(--white); font-weight: 700; font-size: 17px; margin-top: 6px; }
  .badge-raffle .badge-title { color: var(--sky); font-size: 42px; }
  .badge-raffle .badge-text { color: var(--sun); font-weight: 800; font-size: 19px; line-height: 1.4; margin-top: 2px; }
  .badge-service .badge-text { color: var(--white); font-weight: 800; font-size: 21px; line-height: 1.5; }
  .info-band {
    position: absolute; left: 0; top: 1018px; width: 849px; height: 50px; background: var(--sun);
    display: flex; align-items: center; justify-content: center;
    font-family: "Passion One", sans-serif; font-size: 23px; color: var(--white); letter-spacing: 0.2px;
  }
  .sponsors {
    position: absolute; left: 118px; top: 1082px; width: 630px;
    display: grid; grid-template-columns: repeat(8, 1fr); row-gap: 24px; column-gap: 8px;
  }
  .sponsor {
    height: 42px; display: flex; align-items: center; justify-content: center; gap: 4px;
    font-weight: 800; font-size: 10px; line-height: 1.1; color: var(--ink); text-align: center;
  }
  .sponsor .mark { width: 9px; height: 9px; background: var(--sky); flex: none; }
  .sponsor .mark.round { border-radius: 50%; background: var(--sun); }
</style>
</head>
<body>
<main class="poster">
  <div class="hero-photo" role="img" aria-label="Foto: Läuferbeine in blauen Laufschuhen mit neongelben Schnürsenkeln auf grüner Wiese, Stadtsilhouette im Hintergrund"></div>

  <svg class="shapes" width="849" height="1018" viewBox="0 0 849 1018" aria-hidden="true">
    <path d="M0 100 H405 V900 Q405 920 385 920 H0 Z" fill="var(--sky)"/>
    <path d="M0 0 H775 C705 175 565 292 405 292 C235 292 95 225 0 138 Z" fill="var(--sun)"/>
  </svg>

  <h1 class="title">sonnhang im schwung</h1>
  <p class="date">21.6.2020</p>
  <p class="venue">ort: talstation kolbing</p>

  <section class="races">
    <h2 class="races-heading">läufe:</h2>
    <div class="race">
      <p class="race-name">10 km Hauptlauf</p>
      <p class="race-detail">10:30 Uhr<br>(mit Zeitmessung)</p>
    </div>
    <div class="race">
      <p class="race-name">5 km quick 2 easy dash</p>
      <p class="race-detail">10:30 Uhr<br>(ohne Zeitmessung)</p>
    </div>
    <div class="race">
      <p class="race-name">Kinderlauf</p>
      <p class="race-detail">9:30 Uhr<br>(600m &amp; 1050m)</p>
    </div>
  </section>

  <div class="badge badge-prize">
    <p class="badge-title">preisgeld</p>
    <p class="badge-text">für Tagessieg</p>
  </div>
  <div class="badge badge-raffle">
    <p class="badge-title">verlosung</p>
    <p class="badge-text">Laufschuhe<br>zu gewinnen</p>
  </div>
  <div class="badge badge-service">
    <p class="badge-text">Parkplätze &amp;<br>Duschen gratis<br>vorhanden</p>
  </div>

  <p class="info-band">Infos zum Programm &amp; Anmeldung: www.sonnhang-im-schwung.at</p>

  <footer class="sponsors">
    <div class="sponsor">LC Sonnhang</div>
    <div class="sponsor">SC Kolbing</div>
    <div class="sponsor">Talbank Kolbing<span class="mark"></span></div>
    <div class="sponsor">Kraftquell</div>
    <div class="sponsor">Laufwerk</div>
    <div class="sponsor"><span class="mark round"></span>Gemeinde Riedach</div>
    <div class="sponsor">Kletterhalle Kolbing</div>
    <div class="sponsor">Fitpunkt</div>
    <div class="sponsor">Sportkauf</div>
    <div class="sponsor">Haustechnik Lenz</div>
    <div class="sponsor">Versicherung Moser</div>
    <div class="sponsor">Bergsport Alm</div>
    <div class="sponsor"><span class="mark round"></span>Bistro Talstation</div>
    <div class="sponsor">Brauerei Hollen</div>
    <div class="sponsor">Druckerei Berger</div>
    <div class="sponsor">FELDKANTE</div>
  </footer>
</main>
</body>
</html>
```